Sign listing benefits of Wash and Fold Service

Sign 48 inches wide and 24 inches height to showcase service listed above.
Benefits include:
Saves Money
Saves Time
Convenient
Stain Treatment

Looking for something colorful (Blue and white are our business colors) the look of a laundromat business.

```html
<!DOCTYPE html>
<html lang="en">
<head>
<meta charset="utf-8">
<title>Wash and Fold Service Sign</title>
<link rel="stylesheet" href="https://fonts.googleapis.com/css2?family=Bebas+Neue&family=Kaushan+Script&family=Montserrat:wght@700;800&display=swap">
<style>
  :root {
    --page: #e6e6e6;
    --navy: #0a2a7a;
    --blue: #0a5aa8;
    --cyan: #08b2d9;
    --swoosh: #00c8f5;
    --white: #ffffff;
    --orange: #ff6a00;
    --orange-light: #ff9a1a;
    --silver-light: #f6f6f6;
    --silver-dark: #c4c7cb;
    --wicker: #5a3d28;
    --towel: #f2c94c;
  }
  * { margin: 0; padding: 0; box-sizing: border-box; }
  html, body { width: 1200px; height: 1200px; overflow: hidden; }
  body { background: var(--page); position: relative; }

  .sign {
    position: absolute; left: 0; top: 300px;
    width: 1200px; height: 600px;
    background: var(--white);
    overflow: hidden;
  }
  .sign-backdrop { position: absolute; inset: 0; }

  .headline {
    position: absolute; left: 50px; top: 52px;
    font-family: "Bebas Neue", sans-serif;
    font-size: 152px; line-height: 1;
    letter-spacing: 1px;
    color: var(--white);
    text-shadow: 0 4px 8px rgba(0, 20, 70, .45);
    white-space: nowrap;
    z-index: 2;
  }
  .headline-script {
    position: absolute; left: 508px; top: 186px;
    font-family: "Kaushan Script", cursive;
    font-size: 86px; line-height: 1;
    color: var(--white);
    text-shadow: 0 4px 8px rgba(0, 20, 70, .4);
    white-space: nowrap;
    z-index: 2;
  }

  .benefits-label {
    position: absolute; left: 51px; top: 219px;
    width: 422px; height: 77px;
    border: 3px solid var(--white);
    border-radius: 40px;
    background: linear-gradient(90deg, var(--orange), var(--orange-light) 60%, var(--orange));
    display: flex; align-items: center; justify-content: center;
    font-family: "Montserrat", sans-serif; font-weight: 800;
    font-size: 34px; color: var(--white);
  }

  .benefit {
    position: absolute;
    display: flex; align-items: flex-start; gap: 14px;
    font-family: "Montserrat", sans-serif; font-weight: 700;
    font-size: 35px; line-height: 44px;
    color: var(--white);
    text-shadow: 0 2px 4px rgba(0, 20, 70, .35);
  }
  .benefit svg { flex: none; width: 42px; height: 42px; margin-top: 1px; }
  .benefit-money { left: 51px; top: 322px; }
  .benefit-time { left: 51px; top: 387px; }
  .benefit-convenient { left: 386px; top: 322px; }
  .benefit-stain { left: 386px; top: 387px; }

  .washer-visual {
    position: absolute; left: 829px; top: 118px;
    width: 346px; height: 452px;
    border-radius: 6px;
    background: linear-gradient(160deg, var(--silver-light), var(--silver-dark));
  }
  .basket-visual {
    position: absolute; left: 747px; top: 354px;
    width: 198px; height: 219px;
    border-radius: 6px;
    background: linear-gradient(180deg, var(--towel), #c9a27a 55%, var(--wicker) 62%, #3e2a1c);
  }
</style>
</head>
<body>
  <main class="sign">
    <svg class="sign-backdrop" width="1200" height="600" viewBox="0 0 1200 600" aria-hidden="true">
      <defs>
        <linearGradient id="blueField" x1="0" y1="0" x2="1" y2="0.4">
          <stop offset="0" stop-color="#0a2a7a"/>
          <stop offset="0.5" stop-color="#0a5aa8"/>
          <stop offset="1" stop-color="#08b2d9"/>
        </linearGradient>
      </defs>
      <path d="M0,0 H1200 V300 C1080,360 960,520 760,535 C560,555 300,575 0,460 Z" fill="var(--swoosh)"/>
      <path d="M0,0 H1200 V270 C1080,340 960,500 760,518 C560,540 300,555 0,448 Z" fill="url(#blueField)"/>
    </svg>

    <div class="washer-visual" role="img" aria-label="Front-loading washing machine"></div>
    <div class="basket-visual" role="img" aria-label="Wicker basket with a stack of folded towels"></div>

    <h1 class="headline">WASH AND FOLD</h1>
    <div class="headline-script">Service</div>

    <div class="benefits-label">Benefits include:</div>

    <div class="benefit benefit-money">
      <svg viewBox="0 0 42 42"><circle cx="21" cy="21" r="19" fill="var(--orange)" stroke="var(--white)" stroke-width="3"/><path d="M13 21.5 L19 27 L29 15" fill="none" stroke="var(--white)" stroke-width="4.5" stroke-linecap="round" stroke-linejoin="round"/></svg>
      <span>Saves Money</span>
    </div>
    <div class="benefit benefit-time">
      <svg viewBox="0 0 42 42"><circle cx="21" cy="21" r="19" fill="var(--orange)" stroke="var(--white)" stroke-width="3"/><path d="M13 21.5 L19 27 L29 15" fill="none" stroke="var(--white)" stroke-width="4.5" stroke-linecap="round" stroke-linejoin="round"/></svg>
      <span>Saves Time</span>
    </div>
    <div class="benefit benefit-convenient">
      <svg viewBox="0 0 42 42"><circle cx="21" cy="21" r="19" fill="var(--orange)" stroke="var(--white)" stroke-width="3"/><path d="M13 21.5 L19 27 L29 15" fill="none" stroke="var(--white)" stroke-width="4.5" stroke-linecap="round" stroke-linejoin="round"/></svg>
      <span>Convenient</span>
    </div>
    <div class="benefit benefit-stain">
      <svg viewBox="0 0 42 42"><circle cx="21" cy="21" r="19" fill="var(--orange)" stroke="var(--white)" stroke-width="3"/><path d="M13 21.5 L19 27 L29 15" fill="none" stroke="var(--white)" stroke-width="4.5" stroke-linecap="round" stroke-linejoin="round"/></svg>
      <span>Stain<br>Treatment</span>
    </div>
  </main>
</body>
</html>
```